Plate Rally! Digital Order Web App

This is a web app on mobile phone, for consumers to order food inside a restaurant using their phones. we have done up the flow but we need to revamp UI design. pls have a look at our current web on your mobile phone:
https://demo.tavrozi.app/o/KLMV/314725

CURRENT DESIGN.
1. food category on left side, always shown. menu items in list view with image.
2. when we click on an item, there is popup page, to select modifiers, or quantity.
3. order review page(cart page) is quite messy now, need a complete new look.
4 payment page(no need to design, handle by Quellon)
5. order confirmation page. success or error return

DESIGN requirements:
please browse through and click to order with current page above. we have put in lots of thoughts and effort for current flow, the new design should base on this flow.
1. web app. no zoom in/out is allowed for users. responsive html to suit different mobile phone screen size. modern fonts.
2. PAGES needed:
home/welcome page,
well laid out menu items page,
single item page, with add on choice and modifier
cart page(to include recommended items, ordered item list, remove item total, changeable quantity,
confirmation page(success, fail)

DELIVERABLES - responsive html, fonts, images asset such as icons, animation, button images(suitable for commercial use without further third party loyalty fee)
Updates

Hi all if we have left a comment on ur design, please revise accordingly and we will conclude it soon!

Target Market(s)

young diners who order food on their mobile phone.

Industry/Entity Type

Restaurant

Coding

Coded - Design and coding required

Number of Pages Required

5+ page

Colors

Designer to choose colors to be used in the design.

Requirements
Must have
• - lively, appetising colors while making the page easy to read. easy on eyes.
• - consistency. fonts used.
Nice to have
• - 2 color schemes
• - html codes. we will top up if you can deliver coded html.
Should not have
• - should not have more than 3 colors
• - should not have more than 3 different fonts
• - should not use colors that are dull

```html
<!DOCTYPE html>
<html lang="en">
<head>
<meta charset="utf-8">
<title>Plate Rally! – Cart</title>
<link rel="stylesheet" href="https://fonts.googleapis.com/css2?family=Roboto:wght@400;500&family=Noto+Sans+SC:wght@400&display=swap">
<style>
  :root {
    --navy: #222760;
    --orange: #e84e1b;
    --green: #5cb531;
    --band: #f1f1f2;
    --ink: #222;
    --muted: #888;
    --line: #dcdcdc;
    --white: #fff;
  }
  * { margin: 0; padding: 0; box-sizing: border-box; }
  html, body { width: 1200px; height: 3403px; overflow: hidden; background: var(--white); }
  body { position: relative; font-family: "Roboto", "Noto Sans SC", sans-serif; color: var(--ink); }
  .abs { position: absolute; }

  .app-header { left: 0; top: 0; width: 1200px; height: 222px; background: var(--navy); color: var(--white); box-shadow: 0 4px 10px rgba(0,0,0,.25); }
  .status-bar { left: 0; top: 22px; width: 1200px; height: 46px; font-size: 34px; }
  .status-time { left: 0; width: 1200px; text-align: center; top: 0; }
  .status-right { right: 30px; top: 0; display: flex; align-items: center; gap: 10px; }
  .status-left { left: 30px; top: 10px; }
  .page-title { left: 0; width: 1200px; top: 104px; text-align: center; font-size: 59px; font-weight: 400; }
  .back-btn { left: 66px; top: 118px; }

  .section-band { left: 0; width: 1200px; background: var(--band); display: flex; justify-content: space-between; align-items: center; padding: 0 68px; font-size: 36px; letter-spacing: .5px; color: #333; }

  .item-photo { left: 68px; width: 386px; height: 311px; border-radius: 8px; }
  .photo-spicy { background: radial-gradient(circle at 50% 50%, #d9a45a 0%, #c58b3e 40%, #9a9a92 62%, #5a4030 100%); }
  .photo-dumpling { background: radial-gradient(circle at 50% 50%, #e8c7a0 0%, #c63b1c 40%, #b53a22 58%, #ddd 66%, #8e6b55 100%); }
  .photo-soybean { background: radial-gradient(circle at 55% 62%, #4a2614 0%, #5b3018 28%, #b9d889 45%, #9fbf6c 62%, #777 80%, #4b3b2e 100%); }
  .item-name { left: 493px; font-size: 45px; font-weight: 400; }
  .item-name-zh { left: 505px; font-size: 36px; color: var(--muted); font-family: "Noto Sans SC", sans-serif; }
  .item-price { left: 505px; font-size: 39px; }
  .qty-stepper { left: 944px; width: 186px; height: 63px; border: 2px solid #cfe6c2; display: flex; align-items: center; justify-content: space-between; padding: 0 18px; color: var(--green); font-size: 40px; }

  .divider { left: 68px; width: 1062px; height: 2px; background: var(--line); }
  .label { left: 66px; font-size: 36px; color: #333; }
  .field { left: 68px; width: 1062px; border: 2px solid #e2e2e2; border-radius: 8px; background: var(--white); }
  .value-right { right: 70px; font-size: 36px; color: #333; }
  .total-row { font-size: 45px; }

  .btn { left: 68px; width: 1062px; height: 112px; border-radius: 8px; display: flex; align-items: center; justify-content: center; font-size: 45px; font-weight: 500; }
  .btn-primary { background: var(--orange); color: var(--white); }
  .btn-outline { border: 3px solid var(--orange); color: var(--orange); gap: 18px; }
</style>
</head>
<body>
  <header class="abs app-header">
    <div class="abs status-bar">
      <svg class="abs status-left" width="170" height="30" viewBox="0 0 170 30">
        <circle cx="10" cy="14" r="7" fill="#fff"/><circle cx="30" cy="14" r="7" fill="#fff"/>
        <circle cx="50" cy="14" r="7" fill="#fff"/><circle cx="70" cy="14" r="7" fill="#fff"/>
        <circle cx="90" cy="14" r="7" fill="#e84e1b"/>
        <path d="M110 10 a28 28 0 0 1 40 0 M117 17 a18 18 0 0 1 26 0" stroke="#fff" stroke-width="4" fill="none"/>
        <circle cx="130" cy="24" r="4" fill="#fff"/>
      </svg>
      <div class="abs status-time">9:45 AM</div>
      <div class="abs status-right">
        <svg width="34" height="28" viewBox="0 0 34 28"><rect x="0" y="20" width="5" height="8" fill="#fff"/><rect x="9" y="14" width="5" height="14" fill="#fff"/><rect x="18" y="7" width="5" height="21" fill="#fff"/><rect x="27" y="0" width="5" height="28" fill="#fff"/></svg>
        <span>100%</span>
        <svg width="70" height="32" viewBox="0 0 70 32"><rect x="2" y="2" width="60" height="28" rx="8" fill="none" stroke="#fff" stroke-width="3"/><rect x="7" y="7" width="50" height="18" rx="4" fill="#fff"/><rect x="64" y="11" width="4" height="10" rx="2" fill="#fff"/></svg>
      </div>
    </div>
    <svg class="abs back-btn" width="36" height="62" viewBox="0 0 36 62"><path d="M32 4 L6 31 L32 58" stroke="#fff" stroke-width="6" fill="none"/></svg>
    <h1 class="abs page-title">Cart</h1>
  </header>

  <div class="abs section-band" style="top:277px;height:123px;"><span>1. REVIEW YOUR ORDER</span><span>4 ITEM</span></div>

  <div class="abs item-photo photo-spicy" role="img" aria-label="Bowl of Sichuan spicy noodles" style="top:468px;"></div>
  <div class="abs item-name" style="top:508px;">Sichuan Spicy Noodles</div>
  <div class="abs item-name-zh" style="top:573px;">川味麻辣面</div>
  <div class="abs item-price" style="top:653px;">S$7.00</div>
  <div class="abs qty-stepper" style="top:645px;"><span>—</span><span>1</span><span>+</span></div>

  <div class="abs item-photo photo-dumpling" role="img" aria-label="Bowl of dumplings in sour chilli soup" style="top:851px;"></div>
  <div class="abs item-name" style="top:892px;">Dumplings W/ Sour Soup</div>
  <div class="abs item-name-zh" style="top:957px;">酸水(10粒)</div>
  <div class="abs item-price" style="top:1037px;">S$8.80</div>
  <div class="abs qty-stepper" style="top:1029px;"><span>—</span><span>1</span><span>+</span></div>

  <div class="abs item-photo photo-soybean" role="img" aria-label="Noodles with soybean paste and cucumber" style="top:1237px;"></div>
  <div class="abs item-name" style="top:1276px;">Noodles W/ Soybean Paste</div>
  <div class="abs item-name-zh" style="top:1341px;">北炸面</div>
  <div class="abs item-price" style="top:1421px;">S$7.00</div>
  <div class="abs qty-stepper" style="top:1413px;"><span>—</span><span>1</span><span>+</span></div>

  <div class="abs divider" style="top:1624px;"></div>
  <div class="abs label" style="top:1690px;">Remarks for all items</div>
  <div class="abs field" style="top:1784px;height:159px;"></div>

  <div class="abs label" style="top:2014px;">Sub Total</div>
  <div class="abs value-right" style="top:2014px;">S$22.80</div>
  <div class="abs divider" style="top:2112px;"></div>
  <div class="abs label total-row" style="top:2158px;">TOTAL</div>
  <div class="abs value-right total-row" style="top:2158px;">S$22.80</div>

  <div class="abs section-band" style="top:2311px;height:120px;"><span>2. KEY IN MOBILE NO</span></div>
  <div class="abs label" style="top:2490px;">to enjoy member benefits</div>
  <div class="abs field" style="top:2583px;height:96px;"></div>

  <div class="abs section-band" style="top:2774px;height:122px;"><span>3. SELECT A PAYMENT</span></div>

  <div class="abs btn btn-primary" style="top:2968px;">PAY WITH CREDIT CARD</div>
  <div class="abs btn btn-outline" style="top:3128px;">
    <svg width="52" height="34" viewBox="0 0 52 34"><path d="M50 17 H4 M18 3 L4 17 L18 31" stroke="#e84e1b" stroke-width="4" fill="none"/></svg>
    <span>ADD MORE ITEMS</span>
  </div>
</body>
</html>
```